Simple Business Cards for Self-employed Coach

Simple business card with a design that includes the QLT logo.
Using either only the logo color or additional colors that match the logo.

Meridian Guides reach deeply into the past, gathering wisdom from East and West, while still staying current with the frontiers of new discovery in cognitive science, genetics, and other disciplines. see https://www.brightharborpath.example/what-is-integral-coaching/

Target Market(s)

Coaching Clients in Tokyo /Asia; in business organizations, but also outside

Industry/Entity Type

Life Coaching

Contact Information for Business Card

Lukas Brenning
Certified Meridian Guide

3-2-48 Kamiyoshi
Nakarino 164-0392
Tokyo, Japan

Phone: +81 70 4817 5062
E-Mail: lukas.brenning@mailora.example

Font styles to use
Sans Serif

Colors
00a990

Requirements
Must have
• include uploaded logo
• color fitting with QLT logo color
Nice to have
• simple, elegant design
Should not have
• clutter

```html
<!DOCTYPE html>
<html lang="en">
<head>
<meta charset="utf-8">
<title>QLT – Business Card</title>
<link href="https://fonts.googleapis.com/css2?family=Noto+Sans:wght@400;600&display=swap" rel="stylesheet">
<style>
  :root {
    --bg: #cfc9c9;
    --paper: #ffffff;
    --teal: #0b6e67;
    --ink: #3a3a3a;
    --dark: #1e1e1e;
  }
  * { margin: 0; padding: 0; box-sizing: border-box; }
  html, body { width: 1200px; height: 1200px; overflow: hidden; }
  body {
    background: var(--bg);
    position: relative;
    font-family: "Noto Sans", sans-serif;
    color: var(--ink);
  }
  .card {
    position: absolute;
    left: 204px;
    width: 792px;
    height: 462px;
    border-radius: 64px;
    overflow: hidden;
  }
  .card--front { top: 68px; background: var(--paper); }
  .card--back { top: 656px; background: var(--teal); }

  .brand {
    position: absolute;
    display: flex;
    align-items: center;
    font-weight: 600;
    letter-spacing: 6px;
    line-height: 1;
  }
  .brand__mark { display: block; }
  .card--front .brand {
    left: 102px; top: 172px;
    color: var(--teal);
    font-size: 76px;
    gap: 22px;
  }
  .card--front .brand__mark { width: 30px; height: 30px; background: var(--teal); }
  .card--back .brand {
    left: 0; right: 0; top: 188px;
    justify-content: center;
    color: var(--dark);
    font-size: 110px;
    gap: 30px;
  }
  .card--back .brand__mark { width: 42px; height: 42px; background: var(--dark); }

  .identity {
    position: absolute;
    left: 449px; top: 77px;
    border-left: 6px solid var(--teal);
    padding-left: 14px;
    line-height: 1.1;
  }
  .identity__name { font-size: 30px; font-weight: 400; color: var(--ink); }
  .identity__title { font-size: 23px; margin-top: 3px; color: var(--ink); }

  .contact { position: absolute; left: 433px; font-size: 21px; letter-spacing: 0.6px; white-space: nowrap; }
  .contact__icon { position: absolute; left: 0; }
  .contact__text { margin-left: 44px; line-height: 30px; }
  .contact--address { top: 207px; }
  .contact--address .contact__icon { top: 4px; left: 6px; }
  .contact--phone { top: 326px; }
  .contact--phone .contact__icon { top: 2px; }
  .contact--email { top: 387px; font-size: 17px; letter-spacing: 0; }
  .contact--email .contact__icon { top: 6px; left: 2px; }
</style>
</head>
<body>

<section class="card card--front">
  <div class="brand"><span class="brand__mark"></span>QLT</div>

  <div class="identity">
    <h1 class="identity__name">Lukas Brenning</h1>
    <p class="identity__title">Certified Meridian Guide</p>
  </div>

  <div class="contact contact--address">
    <svg class="contact__icon" width="24" height="32" viewBox="0 0 24 32" aria-hidden="true">
      <path d="M12 1C5.9 1 1 5.9 1 12c0 8 11 19 11 19s11-11 11-19C23 5.9 18.1 1 12 1z" fill="#111"/>
      <circle cx="12" cy="12" r="6" fill="#fff"/>
      <circle cx="12" cy="12" r="3.2" fill="#111"/>
    </svg>
    <p class="contact__text">3-2-48 Kamiyoshi<br>Nakarino 164-0392<br>Tokyo, Japan</p>
  </div>

  <div class="contact contact--phone">
    <svg class="contact__icon" width="30" height="30" viewBox="0 0 30 30" aria-hidden="true">
      <circle cx="15" cy="15" r="13.5" fill="none" stroke="#111" stroke-width="2"/>
      <path d="M10 8.5c-1.3 1-2 2.3-1.6 4 1 4 4.6 7.8 8.6 9 1.7.5 3-.2 4-1.4l-2.6-2.6-2 1.2c-2-1-3.7-2.8-4.6-4.7l1.2-2L10.3 8.5z" fill="#111"/>
    </svg>
    <p class="contact__text">+81 70 4817 5062</p>
  </div>

  <div class="contact contact--email">
    <svg class="contact__icon" width="28" height="18" viewBox="0 0 28 18" aria-hidden="true">
      <rect x="1" y="1" width="26" height="16" fill="none" stroke="#111" stroke-width="1.5"/>
      <path d="M1 1l13 10L27 1M1 17l10-8M27 17l-10-8" fill="none" stroke="#111" stroke-width="1.5"/>
    </svg>
    <p class="contact__text">lukas.brenning@mailora.example</p>
  </div>
</section>

<section class="card card--back">
  <div class="brand"><span class="brand__mark"></span>QLT</div>
</section>

</body>
</html>
```